Platinum event Invitation card

This is an invitation to a fund raising event. This will be a Vertical folded card 4.25X6. So the cover and the inside. This is the 70th anniversary of an organization that began in 1949. The organization is a non-profit art gallery, and this event is to help raise money for a new building. For the event, we are using the ideas of "Platinum" and we want to incorporate color.. The final card will need to be in InDesign with a bleed - i have attached template
Updates

A couple things. I am not a big fan of our logo - so would like it smaller on the inside. I also would like to see it different than the orange colors - do not like orange. Not interesting in a big "70" on the front - reminds me of a 70 year birthday card. Looking for something that emphasizes the idea of Platinum and color.. So see the front being shiny platinum/chrome with a color spectrum shining from it. Would like to see the work Evolutionary more prominent.. then 70th anniversary.. more small.

Target Market(s)

Members of the Tilbury Arts Circle and community philanthropists

Requirements
Must have
• Title: 70th Anniversary Platinum Event
• for the save the date card we used:
• EVOLUTIONARY
• Color, Culture, Creativity
• (it would be nice to use that)
• All of this inside the card:
• Thank you to our sponsors - logos attached.
• Wexford Civic Foundation, Fernhollow Savings, Quillmere Health
• (Wexford Civic Foundation is the bigger sponsor)
• 9th Avenue Playhouse
• Saturday, February 9, 2019
• 6:30-8:30pm
• A Benefit for the Tilbury Arts Circle building campaign.
• Dinner, appetizers, and beverages included
• Beer/Wine included in ticket price
• Featuring NBT Orchard and Cellar Studies program
• Food by Marla's Kitchen
• appetizers Gorgonzola Phyllo Cups, Pepper Crusted Pork Tenderloin Crostini
• Dinner
• Pear & Sticky Pecan Salad
• Fresh Baked Rolls
• Chicken with Lemon Chive Sauce
• Roasted Vegetables with Orzo & Feta
• Divine Chocolate Cake with Mocha Frosting
• (Vegetarian option)
• Music by Fine Ltd.
• Silent and Oral Auctions
• Tickets $75 buy online http://tilburyarts.example/gala/ or (555) 218-3306
Nice to have
• I would like the design to be different - but look at:
• http://tilburyarts.example/gala/
• what I would like to see is something like have the card in Platinum/Chrome - with the reflection of a spectrum. My first thought is that the a vertical silver bar on the left side, with reflection of a spectrum going to the right into black.. but can be different than this.
• the logo does not have to be orange - you can use shades of another color.. maybe purple? but very little emphasis on the log (should be quite small)
• Listen to the band on the website. - Could be late 40's swing band type style
• Black background.. chrome/platinum shiny look
• more interest in the front being have chrome look with rainbow reflection over black
Should not have
• A car in it like the save the date card.
• Should not have logo on front of the card.. maybe small on the inside.
• A huge 70
• I put some chrome idea in the file.. and some samples of card looks.. but please don't use them as backgrounds...

```html
<!DOCTYPE html>
<html lang="en">
<head>
<meta charset="utf-8">
<title>70th Anniversary Platinum Event – Invitation</title>
<link rel="stylesheet" href="https://fonts.googleapis.com/css2?family=Anton&family=Open+Sans:wght@300;400;700;800&display=swap">
<style>
  :root {
    --page-bg: #e4e4e6;
    --chrome-light: #f4f4f6;
    --chrome-mid: #b9babd;
    --chrome-dark: #6f7074;
    --rivet: #5c5d61;
    --panel-black: #141416;
    --panel-grey: #3a3c40;
    --flare: rgba(170, 190, 205, 0.28);
    --text-white: #ffffff;
    --text-soft: #e6e6e8;
    --platinum-light: #f2f2f4;
    --platinum-dark: #8e8f93;
    --band-purple: #9b7fc0;
    --band-fade: #e9e1f3;
    --logo-purple: #a583c4;
    --spec-yellow: #f5e35a;
    --spec-peach: #e8b98a;
    --spec-rose: #c98aa0;
    --spec-violet: #a45fb4;
    --sponsor-text: #3b3b40;
  }
  * { box-sizing: border-box; margin: 0; padding: 0; }
  html, body { width: 1200px; height: 800px; overflow: hidden; }
  body {
    background: radial-gradient(ellipse at 50% 40%, #f3f3f4 0%, var(--page-bg) 75%);
    font-family: "Open Sans", Arial, sans-serif;
    position: relative;
  }
  .card {
    position: absolute;
    top: 80px;
    width: 453px;
    height: 640px;
    padding: 22px;
    background: linear-gradient(100deg, var(--chrome-dark) 0%, var(--chrome-light) 18%, var(--chrome-mid) 40%, var(--chrome-light) 62%, var(--chrome-dark) 85%, var(--chrome-mid) 100%);
    box-shadow: 0 10px 24px rgba(0,0,0,0.28);
  }
  .card::before {
    content: "";
    position: absolute;
    inset: 0;
    pointer-events: none;
    background:
      radial-gradient(circle, var(--rivet) 2px, transparent 2.6px) 0 0 / 28px 22px repeat-x,
      radial-gradient(circle, var(--rivet) 2px, transparent 2.6px) 0 100% / 28px 22px repeat-x,
      radial-gradient(circle, var(--rivet) 2px, transparent 2.6px) 0 0 / 22px 28px repeat-y,
      radial-gradient(circle, var(--rivet) 2px, transparent 2.6px) 100% 0 / 22px 28px repeat-y;
  }
  .card--cover { left: 120px; }
  .card--inside { left: 627px; }
  .panel {
    position: relative;
    width: 100%;
    height: 100%;
    overflow: hidden;
    color: var(--text-white);
  }
  .panel__flare {
    position: absolute;
    inset: 0;
    background:
      radial-gradient(ellipse 40% 22% at 20% 25%, var(--flare), transparent 70%),
      radial-gradient(ellipse 38% 20% at 80% 12%, var(--flare), transparent 70%),
      radial-gradient(ellipse 45% 22% at 65% 60%, var(--flare), transparent 70%),
      radial-gradient(ellipse 40% 20% at 25% 88%, var(--flare), transparent 70%),
      linear-gradient(100deg, var(--panel-black) 0%, var(--panel-grey) 45%, var(--panel-black) 70%, #222326 100%);
  }
  .panel__content { position: relative; height: 100%; }

  /* Cover */
  .cover { text-align: center; padding-top: 100px; }
  .cover__year {
    font-weight: 800;
    font-size: 60px;
    line-height: 1;
    background: linear-gradient(180deg, var(--platinum-light) 0%, var(--platinum-dark) 100%);
    -webkit-background-clip: text;
    background-clip: text;
    color: transparent;
  }
  .cover__title {
    font-weight: 800;
    font-size: 38px;
    line-height: 1.02;
    margin-top: 4px;
    text-shadow: 0 2px 4px rgba(0,0,0,0.6);
  }
  .cover__lead {
    font-weight: 300;
    font-size: 18px;
    color: var(--text-soft);
    margin-top: 44px;
  }
  .cover__theme {
    font-family: "Anton", Impact, sans-serif;
    font-size: 66px;
    line-height: 1.05;
    letter-spacing: 0.5px;
    margin-top: 8px;
    background: linear-gradient(90deg, var(--spec-yellow) 0%, var(--spec-peach) 40%, var(--spec-rose) 70%, var(--spec-violet) 100%);
    -webkit-background-clip: text;
    background-clip: text;
    color: transparent;
  }
  .cover__tagline { font-weight: 700; font-size: 19px; margin-top: 2px; }

  /* Inside */
  .inside { padding-top: 20px; }
  .inside__venue { text-align: center; font-weight: 700; font-size: 22px; line-height: 1.1; }
  .inside__date { text-align: center; font-weight: 700; font-size: 16px; color: var(--text-soft); }
  .inside__time {
    margin-top: 4px;
    padding: 2px 0 4px;
    text-align: center;
    font-weight: 800;
    font-size: 34px;
    line-height: 1.1;
    background: linear-gradient(90deg, var(--band-purple) 0%, var(--band-purple) 55%, var(--band-fade) 100%);
  }
  .details {
    list-style: none;
    margin: 14px 6px 0 24px;
    font-size: 10.6px;
    line-height: 1.36;
    color: var(--text-soft);
  }
  .details li { white-space: nowrap; }
  .details li::before { content: "- "; }
  .details li.details__cont::before { content: ""; }
  .inside__tickets { margin: 4px 0 0 22px; font-weight: 700; font-size: 15px; }
  .sponsors {
    position: absolute;
    left: 18px;
    bottom: 24px;
    display: grid;
    grid-template-columns: 96px 66px;
    gap: 6px;
  }
  .sponsor {
    background: #fff;
    color: var(--sponsor-text);
    font-weight: 700;
    font-size: 10px;
    line-height: 1.15;
    display: flex;
    align-items: center;
    justify-content: center;
    text-align: center;
    height: 40px;
    padding: 0 4px;
  }
  .sponsor--lead { grid-column: 1 / 2; }
  .host {
    position: absolute;
    right: 16px;
    bottom: 22px;
    text-align: center;
  }
  .host__name {
    display: flex;
    align-items: center;
    gap: 6px;
    font-weight: 400;
    font-size: 17px;
    color: var(--logo-purple);
    justify-content: center;
  }
  .host__mark { width: 22px; height: 22px; border-radius: 50%; background: var(--logo-purple); }
  .host__phone { font-weight: 800; font-size: 21px; margin-top: 6px; }
</style>
</head>
<body>

<section class="card card--cover" aria-label="Invitation cover">
  <div class="panel">
    <div class="panel__flare" role="img" aria-label="Black background with silvery chrome light-flare streaks"></div>
    <div class="panel__content cover">
      <p class="cover__year">70th</p>
      <h1 class="cover__title">Anniversary<br>Platinum Event</h1>
      <p class="cover__lead">for the save the date card we used:</p>
      <p class="cover__theme">EVOLUTIONARY</p>
      <p class="cover__tagline">Color, Culture, Creativity</p>
    </div>
  </div>
</section>

<section class="card card--inside" aria-label="Invitation inside">
  <div class="panel">
    <div class="panel__flare" role="img" aria-label="Black background with silvery chrome light-flare streaks"></div>
    <div class="panel__content inside">
      <h2 class="inside__venue">9th Avenue Playhouse</h2>
      <p class="inside__date">Saturday, February 9, 2019</p>
      <p class="inside__time">6:30-8:30pm</p>
      <ul class="details">
        <li>A Benefit for the Tilbury Arts Circle building campaign.</li>
        <li>Dinner, appetizers, and beverages included</li>
        <li>Beer/Wine included in ticket price</li>
        <li>Featuring NBT Orchard and Cellar Studies program</li>
        <li>Food by Marla's Kitchen</li>
        <li>appetizers Gorgonzola Phyllo Cups, Pepper Crusted Pork Tenderloin</li>
        <li class="details__cont">Crostini</li>
        <li>Dinner</li>
        <li>Pear &amp; Sticky Pecan Salad</li>
        <li>Fresh Baked Rolls</li>
        <li>Chicken with Lemon Chive Sauce</li>
        <li>Roasted Vegetables with Orzo &amp; Feta</li>
        <li>Divine Chocolate Cake with Mocha Frosting</li>
        <li>(Vegetarian option)</li>
        <li>Music by Fine Ltd.</li>
        <li>Silent and Oral Auctions</li>
      </ul>
      <p class="inside__tickets">Tickets $75 buy online</p>

      <div class="sponsors" aria-label="Sponsors">
        <div class="sponsor">Quillmere Health</div>
        <div class="sponsor">Fernhollow Savings</div>
        <div class="sponsor sponsor--lead">Wexford Civic Foundation</div>
      </div>

      <div class="host">
        <p class="host__name"><span class="host__mark" aria-hidden="true"></span>Tilbury Arts Circle</p>
        <p class="host__phone">(555) 218-3306</p>
      </div>
    </div>
  </div>
</section>

</body>
</html>
```